Birchline Heating & Air

I need a business card made for my company. I would like my new logo for Birchline Heating and Air on the front and my Garage Door on the back.
Front to say -Heating & Air Conditioning , Mini Splits and Heat Pumps, Hydronic In-Floor Heat. Locally Owned and Operated! Licensed, Boned and Insured. Free Estimates on new equipment. 715-408-2159
BGD Back Card, change phone# to 651-374-5810. Remove Commercial and residential and fully sticked vans lines.

```html
<!DOCTYPE html>
<html lang="en">
<head>
<meta charset="utf-8">
<title>Birchline Heating &amp; Air – Business Card</title>
<link href="https://fonts.googleapis.com/css2?family=Montserrat:wght@300;500;600;700;800&display=swap" rel="stylesheet">
<style>
  :root {
    --brand-blue: #0f5289;
    --brand-red: #ec2d24;
    --paper: #ffffff;
    --backdrop: #2a2a2c;
    --ink-blue: #1b4f86;
  }
  * { box-sizing: border-box; margin: 0; padding: 0; }
  html, body { width: 1200px; height: 996px; overflow: hidden; }
  body {
    background: var(--backdrop);
    font-family: "Montserrat", Arial, sans-serif;
    position: relative;
  }
  .card {
    position: absolute;
    top: 148px;
    width: 400px;
    height: 700px;
    border-radius: 30px;
    overflow: hidden;
  }
  .card-front { left: 150px; background: var(--brand-blue); color: var(--paper); }
  .card-back { left: 650px; background: var(--paper); color: var(--ink-blue); }

  /* front */
  .front-wordmark {
    position: absolute; top: 190px; left: 0; right: 0;
    text-align: center; font-weight: 800; color: var(--paper);
    line-height: 1;
  }
  .front-wordmark .name { display: block; font-size: 54px; letter-spacing: 1px; }
  .front-wordmark .trade { display: block; font-size: 27px; margin-top: 10px; letter-spacing: 1px; }
  .service-list {
    position: absolute; top: 430px; left: 48px; right: 20px;
    list-style: none; font-weight: 600; font-size: 19px; line-height: 1.62;
  }
  .service-list li::before {
    content: ""; display: inline-block; width: 6px; height: 6px;
    border-radius: 50%; background: var(--brand-red);
    margin-right: 8px; vertical-align: 8px;
  }
  .bottom-band { position: absolute; left: 0; bottom: 0; width: 400px; height: 40px; }

  /* back */
  .back-wordmark {
    position: absolute; top: 78px; left: 0; right: 0; text-align: center;
    font-weight: 800; color: var(--ink-blue); line-height: 1;
  }
  .back-wordmark .name { display: block; font-size: 50px; letter-spacing: 1px; }
  .back-wordmark .trade { display: block; font-size: 26px; margin-top: 10px; letter-spacing: 2px; }
  .name-band {
    position: absolute; top: 250px; left: 0; width: 100%; height: 96px;
    background: var(--brand-blue); color: var(--paper); text-align: center;
    padding-top: 16px;
  }
  .person-name { font-weight: 700; font-size: 32px; letter-spacing: 2px; line-height: 1.1; }
  .person-role { font-weight: 300; font-size: 20px; letter-spacing: 1px; }
  .contact-icons {
    position: absolute; top: 382px; left: 0; right: 0;
    display: flex; justify-content: center; align-items: center; gap: 12px;
  }
  .contact-icons .rule { width: 80px; height: 1.5px; background: var(--brand-red); margin: 0 10px; }
  .icon-dot {
    width: 30px; height: 30px; border-radius: 50%; background: var(--brand-red);
    display: flex; align-items: center; justify-content: center;
  }
  .contact-lines {
    position: absolute; top: 430px; left: 0; right: 0; text-align: center;
    font-weight: 500; font-size: 17px; line-height: 1.55; color: #2b2b2b;
  }
  .call-box { position: absolute; top: 548px; left: 30px; width: 340px; height: 110px; }
  .call-number {
    position: absolute; top: 28px; left: 112px; font-weight: 800; font-size: 28px;
    color: var(--paper); letter-spacing: 1px;
  }
  .call-note {
    position: absolute; top: 72px; left: 112px; font-weight: 700; font-size: 15px;
    color: var(--paper); letter-spacing: 1px;
  }
</style>
</head>
<body>

<section class="card card-front" aria-label="Front of card">
  <div class="front-wordmark">
    <span class="name">BIRCHLINE</span>
    <span class="trade">HEATING &amp; AIR</span>
  </div>
  <ul class="service-list">
    <li>Heating &amp; Air Conditioning</li>
    <li>Mini Splits and Heat Pumps</li>
    <li>Hydronic In-Floor Heat</li>
    <li>Locally Owned and Operated!</li>
    <li>Licensed, Boned and Insured</li>
  </ul>
  <svg class="bottom-band" viewBox="0 0 400 40" aria-hidden="true">
    <path d="M0 16 H140 L150 4 L160 16 H400 V40 H0 Z" fill="var(--brand-red)"/>
  </svg>
</section>

<section class="card card-back" aria-label="Back of card">
  <div class="back-wordmark">
    <span class="name">BIRCHLINE</span>
    <span class="trade">GARAGE DOOR</span>
  </div>
  <div class="name-band">
    <p class="person-name">DALE NORQUIST</p>
    <p class="person-role">OWNER</p>
  </div>
  <div class="contact-icons">
    <span class="rule"></span>
    <span class="icon-dot">
      <svg width="14" height="14" viewBox="0 0 24 24" aria-label="Phone"><path fill="#fff" d="M6.6 10.8a15 15 0 0 0 6.6 6.6l2.2-2.2a1 1 0 0 1 1-.25 11.4 11.4 0 0 0 3.6.57 1 1 0 0 1 1 1V20a1 1 0 0 1-1 1A17 17 0 0 1 3 4a1 1 0 0 1 1-1h3.5a1 1 0 0 1 1 1c0 1.25.2 2.45.57 3.57a1 1 0 0 1-.25 1z"/></svg>
    </span>
    <span class="icon-dot">
      <svg width="14" height="14" viewBox="0 0 24 24" aria-label="Email"><rect x="2" y="5" width="20" height="14" rx="2" fill="#fff"/><path d="M2 6l10 7 10-7" stroke="var(--brand-red)" stroke-width="2" fill="none"/></svg>
    </span>
    <span class="icon-dot">
      <svg width="14" height="14" viewBox="0 0 24 24" aria-label="Website"><circle cx="12" cy="12" r="9" fill="none" stroke="#fff" stroke-width="2"/><ellipse cx="12" cy="12" rx="4" ry="9" fill="none" stroke="#fff" stroke-width="1.6"/><path d="M3 12h18" stroke="#fff" stroke-width="1.6"/></svg>
    </span>
    <span class="rule"></span>
  </div>
  <div class="contact-lines">
    <p>651-374-5810</p>
    <p>birchlinegaragedoor@mail.com</p>
    <p>www.birchlinegaragedoor.com</p>
  </div>
  <div class="call-box">
    <svg width="340" height="110" viewBox="0 0 340 110" aria-hidden="true">
      <path d="M80 62 H300 L290 100 H70 Z" fill="var(--brand-blue)"/>
      <path d="M90 18 H330 L340 68 H90 Z" fill="var(--brand-red)"/>
      <circle cx="55" cy="55" r="52" fill="var(--paper)" stroke="var(--brand-blue)" stroke-width="3"/>
      <circle cx="55" cy="55" r="42" fill="var(--brand-red)"/>
      <path transform="translate(37 37) scale(1.5)" fill="#fff" d="M6.6 10.8a15 15 0 0 0 6.6 6.6l2.2-2.2a1 1 0 0 1 1-.25 11.4 11.4 0 0 0 3.6.57 1 1 0 0 1 1 1V20a1 1 0 0 1-1 1A17 17 0 0 1 3 4a1 1 0 0 1 1-1h3.5a1 1 0 0 1 1 1c0 1.25.2 2.45.57 3.57a1 1 0 0 1-.25 1z"/>
    </svg>
    <span class="call-number">715-408-2159</span>
    <span class="call-note">24/7 FREE CALL</span>
  </div>
  <svg class="bottom-band" viewBox="0 0 400 40" aria-hidden="true">
    <path d="M0 16 H190 L200 4 L210 16 H400 V40 H0 Z" fill="var(--brand-blue)"/>
  </svg>
</section>

</body>
</html>
```